Business Card Design

I am a realtor and i also flip houses. I am CEO and Founder of my business which is Vantrell Group LLC which is named after my great uncle who died and i was really close to. He was a wonderful friendly man so i want my business to represent him too. My business works with a lot of different people but i want mainly something to show i am a strong confidant woman who owns there own business. I have a really fun personality so i don't want anything TOO serious or manly. I want the perfect mix. My last two business cards i created are too embarrassing to hand out because they are far too girly and i deal with a lot of millionaire clients. I live out in the Palm Springs California area. I think its very important to show i am a single mom, female with her own business at only 24. I don't want to just be a female that blends in with all of the other serious people but yet i don't want to seem immature. People are telling me to stay away from pinks and purples but i don't want blues and greens because they represent men more. But i won't say no to them if there is a happy medium.

Industry/Entity Type

Realtor

Contact Information for Business Card

Vantrell Group, LLC
Corinne Haskett
27385 Sandvale Ave, C2 518
Sable Heights, NV 89915
760-413-6657
Corinnethaskett@mailvern.com

```html
<!DOCTYPE html>
<html lang="en">
<head>
<meta charset="utf-8">
<title>Vantrell Group LLC – Corinne Haskett Business Card</title>
<link rel="stylesheet" href="https://fonts.googleapis.com/css2?family=Turret+Road:wght@500&display=swap">
<style>
  :root {
    --card-dark: #676767;
    --card-light: #958a8f;
    --accent-pink: #ffc9e3;
    --icon-white: #ffffff;
  }
  html, body {
    margin: 0;
    padding: 0;
    width: 1200px;
    height: 702px;
    overflow: hidden;
    background: #ffffff;
  }
  .card {
    position: relative;
    width: 1200px;
    height: 702px;
    background: linear-gradient(90deg, var(--card-dark) 0%, var(--card-light) 55%, var(--card-light) 100%);
    font-family: "Turret Road", sans-serif;
    font-weight: 500;
    font-style: normal;
    color: var(--accent-pink);
    overflow: hidden;
  }
  .accent-stripe {
    position: absolute;
    inset: 0;
  }
  .company-name {
    position: absolute;
    left: 198px;
    top: 214px;
    margin: 0;
    font-size: 50px;
    font-weight: 500;
    letter-spacing: 1px;
    white-space: nowrap;
    transform: translate(-50%, -50%) rotate(-45deg);
  }
  .agent-name {
    position: absolute;
    left: 384px;
    top: 176px;
    margin: 0;
    font-size: 58px;
    font-weight: 500;
    letter-spacing: 1px;
    white-space: nowrap;
    transform: translateY(-50%);
  }
  .postal-address {
    font-style: normal;
  }
  .address-line {
    position: absolute;
    margin: 0;
    font-size: 36px;
    font-style: normal;
    white-space: nowrap;
    transform: translateY(-50%);
    letter-spacing: 0.5px;
  }
  .address-street { left: 462px; top: 325px; }
  .address-unit   { left: 545px; top: 381px; }
  .address-state  { left: 618px; top: 431px; }
  .contact-icon {
    position: absolute;
    fill: var(--icon-white);
    transform: translateY(-50%);
  }
  .icon-phone { left: 318px; top: 562px; }
  .icon-email { left: 314px; top: 629px; }
  .contact-text {
    position: absolute;
    margin: 0;
    font-size: 38px;
    white-space: nowrap;
    transform: translateY(-50%);
    letter-spacing: 0.5px;
  }
  .contact-phone { left: 392px; top: 560px; }
  .contact-email { left: 403px; top: 629px; }
</style>
</head>
<body>
<main class="card">
  <svg class="accent-stripe" width="1200" height="702" viewBox="0 0 1200 702" aria-hidden="true">
    <polygon points="818,0 879,0 1200,312 1200,384" fill="var(--accent-pink)"/>
  </svg>

  <p class="company-name">Vantrell Group LLC</p>

  <h1 class="agent-name">Corinne Haskett</h1>

  <address class="postal-address">
    <p class="address-line address-street">27385 Sandvale Ave</p>
    <p class="address-line address-unit">C2 518 Sable Heights</p>
    <p class="address-line address-state">NV 89915</p>
  </address>

  <svg class="contact-icon icon-phone" width="44" height="44" viewBox="0 0 24 24" aria-hidden="true">
    <path d="M6.6 10.8a15.2 15.2 0 0 0 6.6 6.6l2.2-2.2a1 1 0 0 1 1-.25 11.4 11.4 0 0 0 3.6.57 1 1 0 0 1 1 1V20a1 1 0 0 1-1 1A17 17 0 0 1 3 4a1 1 0 0 1 1-1h3.5a1 1 0 0 1 1 1c0 1.25.2 2.45.57 3.6a1 1 0 0 1-.25 1z"/>
  </svg>
  <p class="contact-text contact-phone">555-413-6657</p>

  <svg class="contact-icon icon-email" width="48" height="34" viewBox="0 0 50 36" aria-hidden="true">
    <rect x="1" y="1" width="48" height="34" fill="var(--icon-white)"/>
    <polyline points="2,2 25,20 48,2" fill="none" stroke="var(--card-dark)" stroke-width="2"/>
    <line x1="2" y1="34" x2="19" y2="16" stroke="var(--card-dark)" stroke-width="2"/>
    <line x1="48" y1="34" x2="31" y2="16" stroke="var(--card-dark)" stroke-width="2"/>
  </svg>
  <p class="contact-text contact-email">corinnethaskett@mailvern.com</p>
</main>
</body>
</html>
```